New online business - used mobile phones - needs unique eye catching web design that sets it apart

The Handset Bazaar
We are a new business looking for a rapid response for our web site design. We don't want a normal website....... we need to be creative - most important PLEASE view the attached files uploaded 3 March to ensure you get us :)
.
The Handset Bazaar buys new and damaged mobile phones from the public. A simple process they complete to sell their mobile to us; we want our website to reflect this.
Our website needs to be modern, edgy and fun, not corporate and definitely not like any other mobile phone buying site in the world today!!
Our name was taken from a play on the share/stock market which we have tried to bring into the design ....... it hasn't worked with early designs submitted. Now taking a different approach. Refer to new attached files which should help you visualise our concept.

We like layout from Sketch Flock – rtlbenoviqs #7132809 design as this is very close to our layout vision.
The first page to tell the public what we do, how we do it, and then they click to accept the instant online quote. (page two they complete details about the mobiles model & condition they are selling, then page three complete their personal details).
Our background preference is dark, blackboard or dark with slight texture
a) We love white on black/dark background either typewriter font or look like hand drawn refer to attached files & heronandfig.com.au site to see. Would Label font work???

b) Where the light blue colour is on #7132809 this needs to be like chromavell colour classic green, fern green or bright green, not fluorescent lime green or an insipid green.

c) The banner says The Handset Bazaar is open........... for buying mobiles for cash $$$ (we need people to know we BUY used/damaged phones)

d) We love colour either solid colour or looks like it has been coloured in on our dark background. Open to white or pastel background versions refer to attached coffee file.
We like Chromavell Orange 021,Haute Red,Dazzling Blue, Cyan Blue, Beetroot Purple, Island Green.
e) How it works – underneath this title put Our deal …………. It’s easy as…………..quote, post, get paid!!!
Quote – first circle hand drawn icon showing mobile phone & $ sign. Underneath it says .....Obtain Quote for Model & Condition
Post – second circle hand drawn icon show parcel. Underneath it says Free Post
Paid – third circle hand drawn icon showing large $ sign. Underneath it says Payment in Two Days
Plans - is swapped for wording- Get Market Quote with a large button which says GO or CLICK HERE (they click on the button & it takes them to the next page)
f) FAQ
Allow for six FAQ’s we will forward correct content to you for final design layout.

g) About Us
Please allow about a paragraph of text here, we will forward correct content to you for final design layout.
h) Contact Us
At the bottom where normal website have ………. home, contact details, blog, etc, please only put Email us & Call us, then social media icons for QV, Work Nest and Chirpel

I) LOGO We don’t have one yet, just put The Handset Bazaar at the top & it needs to be large sized font ................we are new and we need to push our name
If you are not clear on our vision ..........please email me and I will reply very quickly.
Thank you for taking the time to read & understand & get us:)

Target Market(s)

20-45 years any body with a spare smart phone that is lying around and they can get cash for. Target market could be slightly older to 50 but focus of 20-40's

Industry/Entity Type

Business

Number of Pages Required

3 page

Font styles to use
Other font styles liked:
• handwritten font or typewriter font

Requirements
Must have
• Read only attached files dated 4 March, tech error with other files, being removed.
• 1 Layout design of Sketch Flock – rtlbenoviqs #7132809
• 2 Hand drawn icons - refer to files
• 3 White font needs to look like hand written refer to heronandfig.com.au or typewriter font - large size font
• 4 Main colours are Black or dark background, green with white text, preference is hand drawn font. The three circles for quote, post & pay with hand drawn icons can be any colour ...... Purple for quote, orange for post & green for paid
• 5 Big green button underneath 3 circles quote/post/pay - customers click on big button to get instant quote
Nice to have
• Coloured in hand drawings as per file
• Great Hand drawings coloured in
Should not have
• NO template designs so it look like you just put some text & a photo. Don't fill the page with mobile phones, one or two is ok, mobile phone pictures date so fast.
• Cartoons

```html
<!DOCTYPE html>
<html lang="en">
<head>
<meta charset="utf-8">
<title>The Handset Bazaar</title>
<link href="https://fonts.googleapis.com/css2?family=Patrick+Hand&family=Oswald:wght@600&family=Open+Sans:wght@400;700&display=swap" rel="stylesheet">
<style>
  :root {
    --ink: #000000;
    --chalk: #ffffff;
    --green: #93c83e;
    --red: #e2382a;
    --panel: #383838;
    --muted: #8a8a8a;
    --box-brown: #a87a4a;
    --note-green: #8fb99a;
  }
  * { margin: 0; padding: 0; box-sizing: border-box; }
  html, body { width: 754px; height: 1200px; overflow: hidden; background: var(--ink); }
  .page {
    position: relative; width: 754px; height: 1200px; overflow: hidden;
    background:
      radial-gradient(ellipse 420px 340px at 300px 120px, rgba(70,110,60,.45), transparent 70%),
      radial-gradient(ellipse 520px 520px at 377px 300px, #1c1f1c, transparent 75%),
      var(--ink);
    color: var(--chalk);
    font-family: "Patrick Hand", cursive;
  }
  .abs { position: absolute; }
  .brand {
    left: 0; width: 754px; top: 44px; text-align: center;
    font-family: "Oswald", sans-serif; font-weight: 600; font-size: 40px; line-height: 1.05;
    color: var(--chalk); text-transform: uppercase; letter-spacing: 1px;
  }
  .brand .square { display: inline-block; width: 14px; height: 14px; background: var(--green); margin-right: 10px; vertical-align: middle; }
  .headline { left: 0; width: 754px; top: 166px; text-align: center; font-size: 24px; }
  .headline .cash { color: var(--red); }
  .down-arrow { left: 358px; top: 240px; }
  .section-title { left: 0; width: 754px; text-align: center; font-size: 32px; }
  .how-title { top: 296px; }
  .step-art { border-radius: 10px; }
  .art-phone { left: 188px; top: 360px; width: 66px; height: 114px; background: linear-gradient(#555, #2a2a2a); border: 2px solid #9a9a9a; }
  .art-box { left: 310px; top: 358px; width: 134px; height: 112px; background: linear-gradient(160deg, #7a5632, var(--box-brown) 60%, #d9b58a); }
  .art-dollar { left: 504px; top: 384px; width: 60px; height: 102px; background: linear-gradient(#b9d6bf, var(--note-green)); border-radius: 30px; }
  .connectors { left: 0; top: 340px; }
  .step-label {
    top: 502px; width: 180px; text-align: center;
    font-family: "Oswald", sans-serif; font-weight: 600; font-size: 11px; text-transform: uppercase; letter-spacing: .2px;
  }
  .quote-ribbon { left: 178px; top: 546px; }
  .quote-button {
    left: 223px; top: 547px; width: 310px; height: 54px; line-height: 54px; text-align: center;
    font-size: 32px; color: #111; text-decoration: none;
  }
  .faq-title { top: 646px; font-size: 30px; }
  .faq-panel { left: 142px; top: 694px; width: 471px; height: 271px; background: var(--panel); }
  .faq-notch { left: 366px; top: 694px; width: 0; height: 0; border-left: 11px solid transparent; border-right: 11px solid transparent; border-top: 11px solid var(--ink); }
  .faq-divider { left: 377px; top: 700px; height: 259px; border-left: 1px dashed #6a6a6a; }
  .faq-column { top: 712px; width: 185px; font-family: "Open Sans", sans-serif; text-align: center; }
  .faq-column.left { left: 164px; }
  .faq-column.right { left: 398px; top: 716px; }
  .faq-item { height: 83px; }
  .faq-item h3 { font-size: 9.5px; font-weight: 700; margin-bottom: 8px; }
  .faq-item p { font-size: 6.8px; font-weight: 700; line-height: 1.28; }
  .about-title { top: 986px; font-size: 34px; }
  .accent { color: var(--green); }
  .about-text { left: 142px; top: 1032px; width: 480px; font-family: "Open Sans", sans-serif; font-weight: 700; font-size: 7.3px; line-height: 1.3; }
  .contact-title { top: 1082px; font-size: 32px; color: var(--green); }
  .contact-line { left: 142px; display: flex; align-items: center; gap: 8px; font-family: "Open Sans", sans-serif; font-size: 8px; }
  .contact-email { top: 1138px; }
  .contact-phone { top: 1160px; }
  .social { left: 550px; top: 1173px; display: flex; gap: 7px; }
  .social span { width: 14px; height: 14px; background: var(--muted); border-radius: 2px; display: block; }
</style>
</head>
<body>
<main class="page">
  <header>
    <h1 class="abs brand"><span class="square"></span>The Handset Bazaar</h1>
    <p class="abs headline">The Handset Bazaar is Open for <span class="cash">Buying Mobiles for cash!</span></p>
    <svg class="abs down-arrow" width="30" height="50" viewBox="0 0 30 50" aria-hidden="true">
      <path d="M6 2 C4 18, 14 30, 18 44" stroke="#fff" stroke-width="1.6" fill="none"/>
      <path d="M10 38 L18 45 L21 35" stroke="#fff" stroke-width="1.6" fill="none"/>
    </svg>
  </header>

  <section class="how-it-works">
    <h2 class="abs section-title how-title">How it works</h2>
    <svg class="abs connectors" width="754" height="180" viewBox="0 0 754 180" aria-hidden="true">
      <path d="M258 125 C300 120, 280 30, 340 14 C370 8, 380 18, 378 30" stroke="#7fb03a" stroke-width="2" stroke-dasharray="5 4" fill="none"/>
      <path d="M404 130 C410 170, 470 165, 480 120 C488 80, 500 52, 506 60" stroke="#7fb03a" stroke-width="2" stroke-dasharray="5 4" fill="none"/>
    </svg>
    <div class="abs step-art art-phone" role="img" aria-label="Hand drawn mobile phone reading Get Quote"></div>
    <div class="abs step-art art-box" role="img" aria-label="Hand drawn open cardboard parcel"></div>
    <div class="abs step-art art-dollar" role="img" aria-label="Hand drawn large dollar sign"></div>
    <p class="abs step-label" style="left:126px">Model &amp; condition with quote</p>
    <p class="abs step-label" style="left:287px">Free post</p>
    <p class="abs step-label" style="left:444px">Two days with get paid</p>
    <svg class="abs quote-ribbon" width="400" height="58" viewBox="0 0 400 58" aria-hidden="true">
      <polygon points="2,4 40,4 62,29 40,54 2,54 24,29" fill="#c83a22"/>
      <polygon points="398,4 360,4 338,29 360,54 398,54 376,29" fill="#c83a22"/>
      <polygon points="32,1 362,1 346,29 362,56 32,56 48,29" fill="var(--green)"/>
    </svg>
    <a class="abs quote-button" href="#quote">START QUOTE</a>
  </section>

  <section class="faq">
    <h2 class="abs section-title faq-title">FAQ</h2>
    <div class="abs faq-panel"></div>
    <div class="abs faq-notch"></div>
    <div class="abs faq-divider"></div>
    <div class="abs faq-column left">
      <article class="faq-item"><h3>LOREM IPSUM</h3><p>Lorem ipsum dolor sit amet, consectetuer adipiscing elit, sed diam nonummy nibh euismod tincidunt ut laoreet dolore magna aliquam erat volutpat. Ut wisi enim ad minim veniam, quis nostrud exerci tation ullamcorper.</p></article>
      <article class="faq-item"><h3>LOREM IPSUM</h3><p>Lorem ipsum dolor sit amet, consectetuer adipiscing elit, sed diam nonummy nibh euismod tincidunt ut laoreet dolore magna aliquam erat volutpat. Ut wisi enim ad minim veniam, quis nostrud exerci tation ullamcorper.</p></article>
      <article class="faq-item"><h3>LOREM IPSUM</h3><p>Lorem ipsum dolor sit amet, consectetuer adipiscing elit, sed diam nonummy nibh euismod tincidunt ut laoreet dolore magna aliquam erat volutpat. Ut wisi enim ad minim veniam, quis nostrud exerci tation ullamcorper.</p></article>
    </div>
    <div class="abs faq-column right">
      <article class="faq-item"><h3>LOREM IPSUM</h3><p>Lorem ipsum dolor sit amet, consectetuer adipiscing elit, sed diam nonummy nibh euismod tincidunt ut laoreet dolore magna aliquam erat volutpat. Ut wisi enim ad minim veniam, quis nostrud exerci tation ullamcorper.</p></article>
      <article class="faq-item"><h3>LOREM IPSUM</h3><p>Lorem ipsum dolor sit amet, consectetuer adipiscing elit, sed diam nonummy nibh euismod tincidunt ut laoreet dolore magna aliquam erat volutpat. Ut wisi enim ad minim veniam, quis nostrud exerci tation ullamcorper.</p></article>
      <article class="faq-item"><h3>LOREM IPSUM</h3><p>Lorem ipsum dolor sit amet, consectetuer adipiscing elit, sed diam nonummy nibh euismod tincidunt ut laoreet dolore magna aliquam erat volutpat. Ut wisi enim ad minim veniam, quis nostrud exerci tation ullamcorper.</p></article>
    </div>
  </section>

  <section class="about">
    <h2 class="abs section-title about-title"><span class="accent">ABOUT</span> US</h2>
    <p class="abs about-text">Lorem ipsum dolor sit amet, consectetuer adipiscing elit, sed diam nonummy nibh euismod tincidunt ut laoreet dolore magna aliquam erat volutpat. Ut wisi enim ad minim veniam, quis nostrud exerci tation ullamcorper suscipit lobortis nisl ut aliquip ex ea commodo consequat. Duis autem vel eum iriure dolor in hendrerit in vulputate velit</p>
  </section>

  <footer class="contact">
    <h2 class="abs section-title contact-title">CONTACT</h2>
    <p class="abs contact-line contact-email">
      <svg width="17" height="12" viewBox="0 0 17 12" aria-hidden="true"><rect x="0.7" y="0.7" width="15.6" height="10.6" fill="none" stroke="#fff" stroke-width="1.2"/><path d="M1 1 L8.5 7 L16 1" fill="none" stroke="#fff" stroke-width="1.2"/></svg>
      hello@handsetbazaar.example
    </p>
    <p class="abs contact-line contact-phone">
      <svg width="17" height="17" viewBox="0 0 17 17" aria-hidden="true"><path d="M3 1 L6 4 L4.5 6.5 C6 9.5 7.5 11 10.5 12.5 L13 11 L16 14 L13.5 16 C7 15 2 10 1 3.5 Z" fill="none" stroke="#fff" stroke-width="1.2"/></svg>
      08 5550 19273
    </p>
    <div class="abs social">
      <span role="img" aria-label="QV"></span>
      <span role="img" aria-label="Work Nest"></span>
      <span role="img" aria-label="Chirpel"></span>
    </div>
  </footer>
</main>
</body>
</html>
```